Save The Date for 2019 QRP Symposium

We have an annual meeting each June and need a Save the Date (STD) designed. It should be a two-sided postcard with room for address and stamp (according to US Mail postal standards). I have attached some examples from prior years, but we would appreciate a more modern and attractive design for this year's STD.

Target Market(s)

Our own members - nurses, nurse practitioners, PAs and physicians

Industry/Entity Type

Medical

Requirements
Must have
• Must include our logos (attached), ideally in a coordinating fashion - as was done in prior years (see examples attached) and without modifying the logos too much. Needs have the following information:
• - "Save the Date"
• - "The 12th Annual Vascular Crew Roundtable"
• - "Friday, June 7, 2019" or "6/7/19"
• - "The Halvern–Trask Building | 274 West 19th Street | NYC"
• - Please include our website (www.zq-olm.example/events), phone number (212-555-0147) and email address (ask@zq-olm.example) for people to ask questions
• - Must have space for a postage stamp and the name/address of the postcard recipient
Nice to have
• Would be nice to remain in our blue/grey/olive color palate (see attached Brand Standards guide).
Should not have
• Please do not use stock photos of medical staff. Please don't use cartoons or cartoon images (although a tasteful sketch may be considered).

```html
<!DOCTYPE html>
<html lang="en">
<head>
<meta charset="utf-8">
<title>Save the Date – 12th Annual Vascular Crew Roundtable</title>
<link rel="stylesheet" href="https://fonts.googleapis.com/css2?family=Libre+Caslon+Text:wght@400;700&family=Nunito+Sans:wght@400;700;800&display=swap">
<style>
  :root {
    --navy: #15295a;
    --rule: #4a5c86;
    --white: #ffffff;
    --stamp-line: rgba(255, 255, 255, 0.7);
  }
  html, body {
    margin: 0;
    padding: 0;
    width: 1200px;
    height: 927px;
    overflow: hidden;
    background: var(--navy);
  }
  .card {
    position: relative;
    width: 1200px;
    height: 927px;
    background: var(--navy);
    color: var(--white);
    font-family: "Nunito Sans", Arial, sans-serif;
    overflow: hidden;
  }
  .header-rule {
    position: absolute;
    left: 0;
    top: 204px;
    width: 1170px;
    height: 2px;
    background: var(--rule);
  }
  .brand {
    position: absolute;
    left: 45px;
    top: 12px;
    display: flex;
    align-items: center;
  }
  .brand-mark {
    width: 148px;
    height: 148px;
    border: 3px solid var(--white);
    border-radius: 50%;
    box-sizing: border-box;
  }
  .brand-divider {
    width: 2px;
    height: 98px;
    background: var(--white);
    margin: 0 24px 0 30px;
  }
  .brand-name {
    font-family: "Libre Caslon Text", Georgia, serif;
    font-size: 40px;
    font-weight: 400;
    line-height: 1.05;
    margin: 0;
  }
  .brand-sub {
    font-family: "Libre Caslon Text", Georgia, serif;
    font-size: 17px;
    font-weight: 700;
    letter-spacing: 0.5px;
    margin: 14px 0 0;
  }
  .partner-badge {
    position: absolute;
    top: 40px;
    width: 116px;
    height: 116px;
    border: 3px solid var(--white);
    border-radius: 50%;
    box-sizing: border-box;
  }
  .partner-badge.first { left: 895px; }
  .partner-badge.second { left: 1043px; }
  .hero-art {
    position: absolute;
    left: 0;
    top: 284px;
    width: 572px;
    height: 218px;
  }
  .headline {
    position: absolute;
    right: 44px;
    top: 328px;
    text-align: right;
  }
  .save-date {
    margin: 0;
    font-size: 64px;
    font-weight: 800;
    line-height: 1;
    letter-spacing: 0.5px;
  }
  .event-title {
    margin: 20px 0 0;
    font-size: 31px;
    font-weight: 400;
    line-height: 1.35;
    letter-spacing: 0.5px;
  }
  .event-title sup {
    font-size: 18px;
    vertical-align: 14px;
    line-height: 0;
  }
  .address-lines {
    position: absolute;
    left: 58px;
    top: 614px;
    width: 458px;
  }
  .address-line {
    height: 1px;
    background: var(--white);
    margin-bottom: 57px;
  }
  .stamp-box {
    position: absolute;
    left: 574px;
    top: 604px;
    width: 100px;
    height: 120px;
    border: 2px dashed var(--stamp-line);
    box-sizing: border-box;
  }
  .event-details {
    position: absolute;
    right: 44px;
    top: 596px;
    text-align: right;
    font-size: 29px;
    line-height: 46px;
  }
  .event-details p { margin: 0; }
  .event-date { font-weight: 700; }
  .contact {
    position: absolute;
    left: 55px;
    top: 850px;
    margin: 0;
    font-size: 21px;
  }
</style>
</head>
<body>
  <main class="card">
    <header>
      <div class="brand">
        <div class="brand-mark"></div>
        <div class="brand-divider"></div>
        <div>
          <p class="brand-name">Meridian Heart College</p>
          <p class="brand-sub">EMPIRE REGION CHAPTER</p>
        </div>
      </div>
      <div class="partner-badge first"></div>
      <div class="partner-badge second"></div>
    </header>
    <div class="header-rule"></div>

    <svg class="hero-art" viewBox="0 0 572 218" role="img" aria-label="Illustration of a gloved arm reaching out and holding a red heart with a heartbeat line">
      <defs>
        <linearGradient id="heroTone" x1="0" y1="0" x2="1" y2="0">
          <stop offset="0" stop-color="#e3e5ea"/>
          <stop offset="0.35" stop-color="#f3cfa5"/>
          <stop offset="0.55" stop-color="#f2646b"/>
          <stop offset="1" stop-color="#e8404a"/>
        </linearGradient>
      </defs>
      <rect x="0" y="0" width="572" height="218" rx="12" fill="url(#heroTone)" opacity="0.9"/>
    </svg>

    <section class="headline">
      <h1 class="save-date">SAVE THE DATE</h1>
      <p class="event-title">12<sup>th</sup> ANNUAL VASCULAR CREW<br>ROUNDTABLE</p>
    </section>

    <div class="address-lines" aria-label="Recipient address">
      <div class="address-line"></div>
      <div class="address-line"></div>
      <div class="address-line"></div>
    </div>

    <div class="stamp-box" aria-label="Postage stamp area"></div>

    <section class="event-details">
      <p class="event-date">Friday, June 7, 2019</p>
      <p>The Halvern–Trask Building</p>
      <p>274 West 19th Street</p>
      <p>NYC</p>
    </section>

    <p class="contact">For additional information call 212-555-0147 or email ask@zq-olm.example or visit www.zq-olm.example/events</p>
  </main>
</body>
</html>
```